We are an appraisal and dispute resolution company that works with insurance companies and insureds.

We need a website built that appeals to insurance companies as well as insureds to entrust we can assist come to a resolution with their property insurance claim.

Target Market(s)

Insurance Carriers and Insureds

Industry/Entity Type

Insurance

Coding

Coded - Design and coding required

Number of Pages Required

5+ page

Requirements
Must have
• Would like to click on pages and it take you down one page to that specific section
Nice to have
• Clean look

```html
<!DOCTYPE html>
<html lang="en">
<head>
<meta charset="utf-8">
<title>Meridian — Claims Appraisal and Mediation</title>
<link href="https://fonts.googleapis.com/css2?family=Montserrat:wght@400;500;600;700&family=Nunito+Sans:wght@400;600&display=swap" rel="stylesheet">
<style>
:root{
  --teal:#2ec3c3;
  --teal-dark:#22a8ab;
  --navy:#133347;
  --navy-deep:#0e2a3d;
  --ink:#1f2a33;
  --body:#4c555d;
  --muted:#7a8289;
  --white:#ffffff;
}
*{box-sizing:border-box;margin:0;padding:0}
html,body{width:1200px;height:3851px;overflow:hidden}
body{position:relative;font-family:"Nunito Sans",Arial,sans-serif;color:var(--body);background:var(--white)}
a{text-decoration:none;color:inherit}
.abs{position:absolute}
.heading{font-family:"Montserrat",Arial,sans-serif;font-weight:400;color:var(--ink);font-size:35px;letter-spacing:-.5px;white-space:nowrap}
.heading strong{font-weight:700}
.heading .accent{color:var(--teal);font-weight:700}
.rule{position:absolute;height:3px;width:46px;background:var(--teal)}
.btn{position:absolute;display:flex;align-items:center;justify-content:center;background:var(--teal);color:var(--white);font-family:"Montserrat",Arial,sans-serif;font-weight:700;font-size:13px;border-radius:22px;letter-spacing:.3px}
.brand{font-family:"Montserrat",Arial,sans-serif;font-weight:700;display:flex;align-items:center;gap:8px;white-space:nowrap}
.brand-dot{width:9px;height:9px;background:var(--teal)}

/* hero */
.hero-photo{left:0;top:0;width:1200px;height:742px;background:linear-gradient(100deg,#c9cbcc 0%,#8c959b 30%,#4d5a66 55%,#6b7378 80%,#9a9d9d 100%)}
.hero-shade{left:0;top:0;width:1200px;height:742px;background:linear-gradient(180deg,rgba(10,20,30,.45) 0%,rgba(10,20,30,.2) 40%,rgba(10,20,30,.35) 100%)}
.nav{left:0;top:0;width:1200px;height:90px}
.nav .brand{position:absolute;left:122px;top:30px;color:var(--white);font-size:28px;letter-spacing:1px}
.nav-link{position:absolute;top:37px;font-family:"Montserrat",Arial,sans-serif;font-size:13px;font-weight:500;color:var(--white);letter-spacing:.2px}
.nav-link.active{color:var(--teal)}
.nav-link.active::after{content:"";position:absolute;left:50%;top:24px;width:30px;height:2px;margin-left:-15px;background:var(--teal)}
.hero-brand{left:0;top:262px;width:1200px;justify-content:center;color:var(--white);font-size:62px;letter-spacing:4px}
.hero-title{left:0;top:340px;width:1200px;text-align:center;font-family:"Montserrat",Arial,sans-serif;font-weight:600;font-size:45px;line-height:49px;color:var(--white);letter-spacing:1px}
.arrow{top:328px}
.hero-marker{left:588px;top:712px;width:24px;height:24px;background:var(--white)}

/* about */
.about-photo{left:114px;top:837px;width:496px;height:373px;border-radius:0 90px 0 90px;background:linear-gradient(120deg,#e9e3dc 0%,#c8b3a2 40%,#8f7d6c 70%,#50555c 100%)}
.about-frame{left:525px;top:1098px;width:106px;height:130px;border-right:2px solid var(--teal);border-bottom:2px solid var(--teal)}
.eyebrow{left:674px;top:862px;font-family:"Montserrat",Arial,sans-serif;font-size:14px;color:var(--ink)}
.about-title{left:676px;top:884px}
.about-copy{left:676px;top:956px;width:452px;font-size:15px;line-height:25px}
.about-copy p+p{margin-top:25px}

/* services */
.services{left:0;top:1334px;width:1200px;height:608px;background:linear-gradient(180deg,var(--navy-deep) 0%,#175066 35%,#23979f 72%,var(--teal) 100%)}
.services-marker{left:586px;top:1305px;width:28px;height:28px;background:var(--navy-deep)}
.services .heading{position:absolute;left:0;top:58px;width:1200px;text-align:center;color:var(--white)}
.services .rule{left:577px;top:100px}
.services-intro{position:absolute;left:300px;top:122px;width:600px;text-align:center;color:#e3eef2;font-size:15px;line-height:24px}
.card{position:absolute;border:2px solid rgba(255,255,255,.85);text-align:center;color:#eaf4f6}
.card h3{font-family:"Montserrat",Arial,sans-serif;font-weight:700;font-size:19px;color:var(--white);margin-bottom:8px}
.card p{font-size:12.5px;line-height:19px;padding:0 42px}
.card.featured{background:var(--white);outline:6px solid rgba(255,255,255,.55);color:var(--muted)}
.card.featured h3{color:var(--ink)}
.card .icon{position:absolute;left:50%;width:90px;height:90px;margin-left:-45px;border-radius:50%;background:var(--teal);display:flex;align-items:center;justify-content:center}
.card.featured .icon{background:var(--navy)}

/* why */
.why-photo{left:0;top:1942px;width:1200px;height:578px;background:linear-gradient(90deg,#f1f5fa 0%,#eef2f7 38%,#c9ccd0 58%,#8d8176 78%,#5c6f84 100%)}
.why-content{left:0;top:1942px;width:1200px;height:578px}
.why-content .heading{position:absolute;left:115px;top:140px}
.why-content .rule{left:115px;top:184px}
.why-copy{position:absolute;left:115px;top:210px;width:410px;font-size:14.5px;line-height:24.5px}
.why-copy p+p{margin-top:25px}

/* news */
.news-title{left:0;top:2562px;width:1200px;text-align:center}
.news-rule{left:577px;top:2605px}
.news-photo{position:absolute;top:2656px;width:316px;height:217px}
.news-card{position:absolute;top:2833px;width:279px;height:185px;background:var(--white);box-shadow:0 4px 14px rgba(0,0,0,.12);text-align:center;padding-top:22px}
.news-date{font-family:"Montserrat",Arial,sans-serif;font-size:12px;color:var(--teal-dark)}
.news-head{margin-top:9px;font-family:"Montserrat",Arial,sans-serif;font-weight:700;font-size:12.5px;line-height:20px;color:var(--ink)}
.news-text{margin-top:10px;padding:0 38px;font-size:11px;line-height:15.5px;color:var(--muted)}

/* contact */
.contact-photo{left:0;top:3110px;width:1200px;height:547px;background:linear-gradient(100deg,#1c3a55 0%,#1f4160 40%,#22425d 70%,#1a3550 100%)}
.contact-content{left:0;top:3110px;width:1200px;height:547px}
.contact-content .heading{position:absolute;left:0;top:58px;width:1200px;text-align:center;color:var(--white)}
.contact-content .rule{left:579px;top:103px}
.contact-intro{position:absolute;left:0;top:120px;width:1200px;text-align:center;color:#dce4ea;font-size:14.5px}
.field{position:absolute;background:var(--white);font-size:14px;color:#3c444b;padding:16px 20px;line-height:18px}

/* footer */
.footer{left:0;top:3657px;width:1200px;height:194px;background:var(--white)}
.footer .brand{position:absolute;left:0;top:44px;width:1200px;justify-content:center;color:var(--navy);font-size:30px;letter-spacing:1px}
.foot-link{position:absolute;top:116px;font-family:"Montserrat",Arial,sans-serif;font-size:13px;font-weight:600;color:var(--ink)}
.copyright{position:absolute;left:0;top:146px;width:1200px;text-align:center;font-size:11.5px;color:var(--muted)}
</style>
</head>
<body>

<section id="home">
  <div class="abs hero-photo" role="img" aria-label="Photo of an appraiser in a suit handing a clipboard to a client across an office desk"></div>
  <div class="abs hero-shade"></div>
  <nav class="abs nav">
    <a class="brand" href="#home">MERIDIAN<span class="brand-dot"></span></a>
    <a class="nav-link active" href="#about" style="left:366px">ABOUT US</a>
    <a class="nav-link" href="#services" style="left:497px">OUR SERVICES</a>
    <a class="nav-link" href="#why" style="left:659px">WHY CHOOSE US</a>
    <a class="nav-link" href="#news" style="left:840px">TESTIMONIALS</a>
    <a class="nav-link" href="#contact" style="left:1001px">CONTACT US</a>
  </nav>
  <div class="abs brand hero-brand">MERIDIAN</div>
  <h1 class="abs hero-title">MERIDIAN CLAIMS APPRAISAL<br>AND MEDIATION</h1>
  <a class="btn" href="#contact" style="left:514px;top:457px;width:179px;height:42px">CONTACT US</a>
  <svg class="abs arrow" style="left:22px" width="24" height="40" viewBox="0 0 24 40"><path d="M20 3 4 20l16 17" fill="none" stroke="#fff" stroke-width="4"/></svg>
  <svg class="abs arrow" style="left:1142px" width="24" height="40" viewBox="0 0 24 40"><path d="M4 3l16 17L4 37" fill="none" stroke="#fff" stroke-width="4"/></svg>
  <div class="abs hero-marker"></div>
</section>

<section id="about">
  <div class="abs about-frame"></div>
  <div class="abs about-photo" role="img" aria-label="Photo of a smiling couple meeting an adviser who shows them a tablet"></div>
  <p class="abs eyebrow">WHO WE ARE</p>
  <h2 class="abs heading about-title">ABOUT <span class="accent">MERIDIAN</span></h2>
  <span class="rule" style="left:676px;top:928px"></span>
  <div class="abs about-copy">
    <p>Lorem Ipsum is simply dummy text of the printing and typesetting industry. Lorem Ipsum has been the industry's standard dummy text ever since the 1500s, when an unknown printer took a galley of type and scrambled it to make a type specimen Lorem Ipsum is simply dummy text of the printing and typesetting</p>
    <p>Lorem Ipsum has been the industry's standard dummy text ever since the 1500s, when an unknowLorem Ipsum is simply dummy text of the printing and typesetting industry.</p>
  </div>
</section>

<section id="services">
  <div class="abs services">
    <h2 class="heading">OUR <strong>SERVICES</strong></h2>
    <span class="rule"></span>
    <p class="services-intro">Lorem Ipsum is simply dummy text of the printing and typesetting industry. Lorem Ipsum has been the industry's standard dummy text ever</p>

    <div class="card" style="left:118px;top:259px;width:308px;height:243px;padding-top:62px">
      <div class="icon" style="top:-45px">
        <svg width="40" height="40" viewBox="0 0 40 40" fill="none" stroke="#fff" stroke-width="2"><circle cx="12" cy="14" r="5"/><circle cx="28" cy="14" r="5"/><path d="M3 34c0-6 4-10 9-10s9 4 9 10M19 34c0-6 4-10 9-10s9 4 9 10"/></svg>
      </div>
      <h3>CONSULTING</h3>
      <p>Lorem Ipsum is simply dummy text of the printing and typesetting industry. Lorem Ipsum has been the industry's Lorem Ipsum is simply dummy text of the printing and typesetting</p>
    </div>

    <div class="card featured" style="left:433px;top:242px;width:338px;height:274px;padding-top:88px">
      <div class="icon" style="top:-36px">
        <svg width="40" height="40" viewBox="0 0 40 40" fill="none" stroke="#fff" stroke-width="2"><rect x="12" y="4" width="16" height="12"/><circle cx="11" cy="24" r="4"/><circle cx="29" cy="24" r="4"/><path d="M3 37c0-5 3-8 8-8s8 3 8 8M21 37c0-5 3-8 8-8s8 3 8 8"/></svg>
      </div>
      <h3>DISPUTE RESOLUTION</h3>
      <p>Lorem Ipsum is simply dummy text of the printing and typesetting industry. Lorem Ipsum has been the industry's Lorem Ipsum is simply dummy text of the printing and typesetting</p>
    </div>

    <div class="card" style="left:783px;top:259px;width:306px;height:243px;padding-top:62px">
      <div class="icon" style="top:-45px">
        <svg width="40" height="40" viewBox="0 0 40 40" fill="none" stroke="#fff" stroke-width="2"><path d="M8 4h18l6 6v26H8z"/><path d="M13 14h14M13 20h14M13 26h9"/></svg>
      </div>
      <h3>APPRAISAL</h3>
      <p>Lorem Ipsum is simply dummy text of the printing and typesetting industry. Lorem Ipsum has been the industry's Lorem Ipsum is simply dummy text of the printing and typesetting</p>
    </div>
  </div>
  <div class="abs services-marker"></div>
</section>

<section id="why">
  <div class="abs why-photo" role="img" aria-label="Photo of an older couple reviewing paperwork with an adviser at a table, fading into a pale background on the left"></div>
  <div class="abs why-content">
    <h2 class="heading">WHY <strong>CHOOSE</strong> <span class="accent">MERIDIAN</span></h2>
    <span class="rule"></span>
    <div class="why-copy">
      <p>Lorem Ipsum is simply dummy text of the printing and typesetting industry. Lorem Ipsum has been the industry's standard dummy text ever since the 1500s, when an unknown printer took a galley of type and scrambled it to make a type specimen Lorem Ipsum is simply dummy</p>
      <p>Lorem Ipsum has been the industry's standard dummy text ever since the 1500s, when an unknow</p>
    </div>
  </div>
</section>

<section id="news">
  <h2 class="abs heading news-title">LATEST <span class="accent">NEWS</span></h2>
  <span class="rule news-rule"></span>

  <div class="news-photo" style="left:102px;background:linear-gradient(135deg,#1d3a4c,#5a7a8a 55%,#c99a5a)" role="img" aria-label="Photo of two business people shaking hands"></div>
  <div class="news-photo" style="left:439px;background:linear-gradient(135deg,#d9dcdd,#7e8a94 50%,#2c3e52)" role="img" aria-label="Photo of an adviser handing a clipboard to a client"></div>
  <div class="news-photo" style="left:777px;background:linear-gradient(135deg,#e8e2d6,#c8a57a 50%,#8a8f6a)" role="img" aria-label="Photo of a family holding a cardboard roof over their heads"></div>

  <article class="news-card" style="left:120px">
    <p class="news-date">JUN 09, 2021</p>
    <h3 class="news-head">LOREM IPSUM IS SIMPLY DUMMY<br>TEXT OF THE PRINTING</h3>
    <p class="news-text">Lorem Ipsum has been the industry's standard dummy text ever since the 1500s, when an unknown</p>
  </article>
  <article class="news-card" style="left:457px">
    <p class="news-date">JUN 09, 2021</p>
    <h3 class="news-head">LOREM IPSUM IS SIMPLY DUMMY<br>TEXT OF THE PRINTING</h3>
    <p class="news-text">Lorem Ipsum has been the industry's standard dummy text ever since the 1500s, when an unknown</p>
  </article>
  <article class="news-card" style="left:795px">
    <p class="news-date">JUN 09, 2021</p>
    <h3 class="news-head">LOREM IPSUM IS SIMPLY DUMMY<br>TEXT OF THE PRINTING</h3>
    <p class="news-text">Lorem Ipsum has been the industry's standard dummy text ever since the 1500s, when an unknown</p>
  </article>
</section>

<section id="contact">
  <div class="abs contact-photo" role="img" aria-label="Dark blue tinted photo of people in a meeting behind the contact form"></div>
  <div class="abs contact-content">
    <h2 class="heading">CONTACT <span class="accent">US</span></h2>
    <span class="rule"></span>
    <p class="contact-intro">Lorem Ipsum has been the industry's standard dummy text ever since the 1500s</p>
    <div class="field" style="left:244px;top:174px;width:354px;height:49px">First Name</div>
    <div class="field" style="left:610px;top:174px;width:354px;height:49px">Last Name</div>
    <div class="field" style="left:244px;top:235px;width:354px;height:48px">Email</div>
    <div class="field" style="left:610px;top:235px;width:354px;height:48px">Phone</div>
    <div class="field" style="left:244px;top:295px;width:720px;height:98px">Message</div>
    <a class="btn" href="#contact" style="left:514px;top:416px;width:179px;height:40px">SUBMIT NOW</a>
  </div>
</section>

<footer class="abs footer">
  <div class="brand">MERIDIAN<span class="brand-dot"></span></div>
  <a class="foot-link" href="#home" style="left:277px">HOME</a>
  <a class="foot-link" href="#about" style="left:372px">ABOUT</a>
  <a class="foot-link" href="#services" style="left:473px">OUR SERVICES</a>
  <a class="foot-link" href="#why" style="left:628px">WHY US?</a>
  <a class="foot-link" href="#news" style="left:743px">BLOG</a>
  <a class="foot-link" href="#contact" style="left:834px">CONTACT US</a>
  <p class="copyright">Copyright 2021 Meridian All Right Rerserved</p>
</footer>

</body>
</html>
```